Redesign Home Page

We need a new home page with a white background. Our company provides singing instruction to students world wide, both in person and on line. We're looking for a very clean and open design with maximum white space. The main goal of the page will be to get users to sign up for our mailing list. The current site is www.kelvarsong.com. I think the new page can be a long page (scrolll down is ok), to allow for more white space while still using the text from the current page.
Updates

Project Deadline Extended
Reason: Hello to all Designers, I apologize for not giving feedback this weekend. We went out of town for the Memorial Day holiday and I had no internet. I will be extending the deadline to Thursday. -Marcus

Target Market(s)

Singers of all ages and abilities, especially beginners.

Industry/Entity Type

It Company

Requirements
Must have
• 1. A white background
2. Lots of open space
3. An email sign up form on the top right that reads:
a. “Improve Your Singing Now.
b. Sign up for our Free Video Series: Tone Pathway
4. Testimonails: found on https://www.kelvarsong.com/tone-ascent
5. My logo with the piano
6. My photo
7. Learn about our Lessons in:
a. San Francisco
b. Alameda
8. On Line Programs:
a. Tone Ascent
b. Zelvo Lessons

Nice to have
• Link to current student page: http://kelvarsong.com/what-students-say/students2
Pictures of singers
Video box: Use Marcus_Example
Should not have
• See "KelvarSong Redesign" file for more details.

```html
<!DOCTYPE html>
<html lang="en">
<head>
<meta charset="utf-8">
<title>MarcusKelvar School of Voice</title>
<link rel="stylesheet" href="https://fonts.googleapis.com/css2?family=Open+Sans:wght@400;600&display=swap">
<style>
  :root {
    --brand-blue: #29a8df;
    --brand-blue-dark: #1f8fc4;
    --ink: #1a1a1a;
    --ink-soft: #333333;
    --logo-ink: #3a3a3a;
    --paper: #ffffff;
    --band-grey: #f3f3f3;
    --field-border: #8a8a8a;
    --panel-text: #eaf6fc;
  }
  * { box-sizing: border-box; margin: 0; padding: 0; }
  html, body {
    width: 1200px; height: 900px; overflow: hidden;
    background: var(--paper);
    font-family: "Open Sans", sans-serif;
    color: var(--ink);
  }
  .page { position: relative; width: 1200px; height: 900px; }

  .brand { position: absolute; left: 90px; top: 14px; display: flex; align-items: center; gap: 10px; }
  .brand-mark { width: 52px; height: 52px; border: 3px solid var(--brand-blue); border-radius: 50%; }
  .brand-text { line-height: 1; }
  .brand-name { font-size: 26px; font-weight: 600; color: var(--logo-ink); letter-spacing: -0.3px; }
  .brand-tagline { font-size: 13px; color: var(--logo-ink); margin-top: 3px; padding-left: 16px; }

  .main-nav { position: absolute; top: 0; left: 660px; display: flex; }
  .main-nav a {
    display: block; height: 52px; padding-top: 26px;
    font-size: 15px; color: var(--ink); text-decoration: none; text-align: center;
  }
  .main-nav .nav-home { width: 71px; background: var(--brand-blue); color: var(--paper); }
  .main-nav .nav-voice { width: 136px; }
  .main-nav .nav-about { width: 46px; }
  .main-nav .nav-contact { width: 136px; }
  .social { position: absolute; top: 23px; left: 1040px; display: flex; gap: 2px; }
  .social span { display: block; width: 26px; height: 26px; background: var(--brand-blue); }

  .hero-photo {
    position: absolute; left: 80px; top: 70px; width: 620px; height: 653px;
    background: radial-gradient(ellipse at 45% 45%, #e8cfc0 0%, #c9a58f 30%, #8a6a55 55%, #f4f1ee 80%, #ffffff 100%);
  }

  .signup { position: absolute; left: 713px; top: 99px; }
  .signup-row { display: flex; align-items: center; }
  .signup-label { font-size: 19px; margin-right: 9px; }
  .signup-field { width: 248px; height: 34px; border: 1px solid var(--field-border); border-right: none; background: var(--paper); }
  .signup-button {
    width: 37px; height: 34px; background: var(--brand-blue); color: var(--paper);
    border: 1px solid var(--brand-blue-dark); font: 14px "Open Sans", sans-serif;
  }
  .signup-points { list-style: none; margin-top: 10px; font-size: 14px; line-height: 18px; }
  .signup-points li { position: relative; padding-left: 15px; }
  .signup-points li::before {
    content: ""; position: absolute; left: 0; top: 7px; width: 7px; height: 7px;
    border-radius: 50%; background: var(--brand-blue);
  }

  .course-panel { position: absolute; left: 711px; top: 274px; width: 393px; height: 450px; background: var(--brand-blue); }
  .course-product {
    position: absolute; left: 888px; top: 190px; width: 202px; height: 170px;
    background: linear-gradient(135deg, #3a3f8f 0%, #6b2d7a 45%, #1b1f3a 100%);
    border-radius: 4px;
  }
  .course-intro {
    position: absolute; left: 722px; top: 368px; width: 372px;
    font-size: 12.6px; line-height: 18.5px; text-align: center; text-transform: uppercase;
    color: var(--panel-text);
  }
  .course-video {
    position: absolute; left: 716px; top: 436px; width: 382px; height: 232px;
    background: radial-gradient(ellipse at 50% 10%, #cfe6ff 0%, #3f7cc8 30%, #10294f 70%, #040a18 100%);
  }
  .course-video svg { position: absolute; left: 149px; top: 75px; }
  .see-more {
    position: absolute; left: 1003px; top: 682px; width: 86px; height: 29px;
    background: var(--paper); color: var(--brand-blue-dark); font-size: 14px;
    text-align: center; line-height: 28px; text-decoration: none;
  }

  .advantages { position: absolute; left: 0; top: 723px; width: 1200px; height: 177px; background: var(--band-grey); }
  .advantages-title { position: absolute; left: 346px; top: 48px; font-size: 22px; font-weight: 400; }
  .advantages-body { position: absolute; left: 347px; top: 78px; width: 486px; font-size: 10.4px; line-height: 14.5px; color: var(--ink-soft); }
  .advantage-tabs { position: absolute; top: 174px; left: 100px; display: flex; gap: 18px; }
  .advantage-tabs span { display: block; width: 183px; height: 4px; background: var(--brand-blue); }
  .advantage-tabs span:first-child { background: #2477c9; }
</style>
</head>
<body>
<div class="page">
  <header>
    <div class="brand">
      <span class="brand-mark"></span>
      <div class="brand-text">
        <div class="brand-name">MarcusKelvar</div>
        <div class="brand-tagline">School of Voice</div>
      </div>
    </div>
    <nav class="main-nav">
      <a class="nav-home" href="#">home</a>
      <a class="nav-voice" href="#">voice</a>
      <a class="nav-about" href="#">about</a>
      <a class="nav-contact" href="#">contact</a>
    </nav>
    <div class="social"><span></span><span></span></div>
  </header>

  <div class="hero-photo" role="img" aria-label="Photo of a young woman singing joyfully into a vintage silver microphone"></div>

  <form class="signup">
    <div class="signup-row">
      <label class="signup-label" for="newsletter-email">Newsletter</label>
      <input class="signup-field" id="newsletter-email" type="email">
      <button class="signup-button" type="button">OK</button>
    </div>
    <ul class="signup-points">
      <li>Improve Your Singing Now</li>
      <li>Sign up for our Free Video Series: Tone Pathway</li>
    </ul>
  </form>

  <section class="course-panel"></section>
  <div class="course-product" role="img" aria-label="Tone Ascent multimedia singing course box set and discs"></div>
  <p class="course-intro">Professional vocal coach, Marcus D. Kelvar has laid the vocal foundation for thousands of singers worldwide, for 20+ years</p>
  <div class="course-video" role="img" aria-label="Video still of a concert crowd raising their hands under stage lights">
    <svg width="84" height="84" viewBox="0 0 84 84" aria-hidden="true">
      <circle cx="42" cy="42" r="41" fill="rgba(255,255,255,0.55)"/>
      <polygon points="32,22 64,42 32,62" fill="#ffffff"/>
    </svg>
  </div>
  <a class="see-more" href="#">see more</a>

  <section class="advantages">
    <h2 class="advantages-title">ADVANTAGES of working with Tone Ascent</h2>
    <p class="advantages-body">After many years of work, I've decided that the effective transformation of the human voice is my life's work and passion. While on line methods of instruction are not a as effective as in person lessons, I find that getting a foundational understanding of the voice that comes with Tone Ascent can greatly enhance your singing voice, whether you're currently studying with a teacher or working on your own.</p>
    <div class="advantage-tabs"><span></span><span></span><span></span><span></span><span></span></div>
  </section>
</div>
</body>
</html>
```